Flyer for a mint vending business (QMT). Draft included... need creative mind to complete!

This flyer will be for a mint vending machine business. I am the owner and the flyer will be given to business owners who will be placing the machines in their business for information on the placement. The flyer will be 6" x 9" so the verbiage needs to fit within the size and be readable. I have included a draft of the basic design (both front and back). I would like it to be colorful and eye-catching but professional. I have included the main image of the mint machine (for the front page) in the uploaded files. The QMT logo mentioned on page two is from the business card (also uploaded). The mint image (page one) can be a stock image- would like it to be round, in a silver wrapper and say "Mint" on the front. The information blurbs on the front surrounding the image should have some form of starburst around the text (as shown in the copy with handwritten notes). Creativity input on font, color and background from the designer is appreciated.

```html
<!DOCTYPE html>
<html lang="en">
<head>
<meta charset="utf-8">
<title>Quill Mint Trading – Mint Machines Flyer</title>
<link href="https://fonts.googleapis.com/css2?family=Montserrat:wght@400;500;600;700;800&display=swap" rel="stylesheet">
<style>
  :root {
    --green-deep: #127a5c;
    --green: #22a07c;
    --green-mid: #3fb892;
    --mint-light: #86d3b6;
    --mint-pale: #e4f4ee;
    --paper: #ffffff;
    --ink-grey: #5a5f5d;
    --logo-grey: #b4b9b8;
    --badge-yellow: #f6c518;
    --backdrop: #e7e9e8;
    --choc: #4a2c1f;
    --machine-red: #c9272c;
  }
  * { box-sizing: border-box; margin: 0; padding: 0; }
  html, body { width: 1200px; height: 900px; overflow: hidden; }
  body {
    background: var(--backdrop);
    font-family: "Montserrat", Arial, sans-serif;
    position: relative;
  }
  .flyer {
    position: absolute;
    top: 45px;
    width: 540px;
    height: 810px;
    background: var(--paper);
    overflow: hidden;
    box-shadow: 0 4px 18px rgba(0,0,0,.12);
  }
  .flyer--front { left: 40px; }
  .flyer--back { left: 620px; }
  .flyer__shapes { position: absolute; inset: 0; }
  .flyer > *:not(.flyer__shapes) { position: absolute; }

  .brand-mark {
    top: 22px; right: 22px;
    width: 88px; height: 88px;
    border-radius: 50%;
    background: var(--logo-grey);
    display: flex; align-items: center; justify-content: center;
    color: #fff; font-weight: 800; font-size: 26px; letter-spacing: 1px;
  }
  .photo { border-radius: 8px; }

  /* front */
  .front-title {
    left: 30px; top: 58px;
    color: #fff; font-weight: 800; font-size: 54px; line-height: .98;
    text-transform: uppercase;
  }
  .leaf-art { left: 190px; top: 40px; width: 80px; height: 58px;
    background: linear-gradient(135deg, #6fc47a, #2e8a45); border-radius: 50% 10px 50% 10px; }
  .front-subtitle { left: 30px; top: 190px; color: #fff; font-size: 15px; font-weight: 500; line-height: 1.3; }
  .choc-photo { left: 32px; top: 262px; width: 120px; height: 62px;
    background: radial-gradient(ellipse at 60% 40%, #7a4c34, var(--choc)); border-radius: 30px; }
  .front-blurb { left: 30px; top: 342px; width: 315px; color: #fff; font-size: 13px; font-weight: 500; line-height: 1.3; }
  .machine-stand-photo { left: 375px; top: 150px; width: 135px; height: 540px;
    background: linear-gradient(180deg, #d8dcdc 0%, #8fc79a 12%, var(--machine-red) 28%, #a91f24 36%, #2a2a2a 40%, #1a1a1a 100%);
    border-radius: 10px 10px 60px 60px; }

  .features { left: 30px; top: 436px; width: 330px; list-style: none; }
  .feature { display: flex; gap: 10px; margin-bottom: 7px; align-items: flex-start; }
  .feature__icon { flex: 0 0 36px; height: 36px; border-radius: 50%; background: var(--mint-pale);
    border: 2px solid var(--green-mid); display: flex; align-items: center; justify-content: center; }
  .feature__title { color: var(--green); font-weight: 700; font-size: 14px; line-height: 1.2; }
  .feature__text { color: var(--ink-grey); font-size: 11px; line-height: 1.25; }

  .support-badge { left: 362px; top: 590px; width: 150px; height: 150px; }
  .support-badge__text { position: absolute; inset: 28px 22px; text-align: center; display: flex; flex-direction: column; justify-content: center; color: #fff; }
  .support-badge__head { font-weight: 800; font-size: 12px; line-height: 1.15; margin-bottom: 4px; }
  .support-badge__note { font-size: 8.5px; font-weight: 600; line-height: 1.2; }

  .contact { left: 30px; bottom: 14px; color: #fff; }
  .contact__names { font-weight: 700; font-size: 14px; line-height: 1.2; }
  .contact__line { font-size: 11.5px; line-height: 1.35; }

  /* back */
  .back-title { left: 30px; top: 52px; color: #fff; font-weight: 800; text-transform: uppercase; line-height: 1; }
  .back-title__small { display: block; font-size: 34px; }
  .back-title__big { display: block; font-size: 54px; }
  .back-intro { left: 30px; top: 170px; width: 330px; color: #fff; font-size: 14px; font-weight: 500; line-height: 1.35; }
  .veterans { left: 30px; top: 262px; width: 300px; color: #fff; }
  .veterans__head { display: flex; align-items: center; gap: 10px; font-weight: 800; font-size: 13px; line-height: 1.15; text-transform: uppercase; }
  .veterans__text { margin-top: 10px; font-size: 12px; line-height: 1.3; font-weight: 500; }
  .machine-photo { left: 335px; top: 235px; width: 175px; height: 285px;
    background: linear-gradient(180deg, #dfe2e2 0%, #9fd0a4 30%, #c7cbcb 62%, var(--machine-red) 72%, #a91f24 100%);
    border-radius: 12px; }
  .bonus { left: 30px; top: 395px; width: 295px; }
  .bonus__heading { color: var(--green); font-weight: 600; font-size: 22px; line-height: 1.2; padding-bottom: 8px; border-bottom: 1.5px solid var(--green-mid); }
  .bonus__lead { margin-top: 12px; color: var(--green); font-weight: 700; font-size: 13.5px; }
  .bonus__text { color: var(--green); font-size: 13.5px; line-height: 1.35; }
  .service-note { left: 30px; top: 588px; width: 480px; color: var(--ink-grey); font-size: 12px; line-height: 1.4; text-align: justify; }
  .chocs-photo { left: 320px; top: 645px; width: 200px; height: 72px;
    background: radial-gradient(ellipse at 50% 45%, #7a4c34, var(--choc)); border-radius: 40px; }
</style>
</head>
<body>

<section class="flyer flyer--front">
  <svg class="flyer__shapes" viewBox="0 0 540 810" aria-hidden="true">
    <defs>
      <linearGradient id="headFront" x1="0" y1="0" x2="1" y2="1">
        <stop offset="0" stop-color="#2aa884"/><stop offset="1" stop-color="#137d5e"/>
      </linearGradient>
    </defs>
    <path d="M0 0H540V235C400 285 220 300 0 335Z" fill="url(#headFront)"/>
    <path d="M0 335C220 300 400 285 540 235V310C400 370 220 405 0 428Z" fill="#7fcfb0"/>
    <path d="M0 428C220 405 400 370 540 310V330C400 390 220 420 0 436Z" fill="#e4f4ee"/>
    <path d="M0 712C180 695 380 700 540 725V810H0Z" fill="#7fcfb0"/>
    <path d="M0 722C180 705 380 712 540 740V810H0Z" fill="url(#headFront)"/>
  </svg>

  <div class="brand-mark">QMT</div>
  <h1 class="front-title">Mint<br>Machines</h1>
  <div class="leaf-art photo" role="img" aria-label="Fresh mint leaves"></div>
  <p class="front-subtitle">The highlights in a mint wrapper!<br>(Or a nutshell as some would say)</p>
  <div class="choc-photo" role="img" aria-label="Chocolate mint patty cut in half"></div>
  <p class="front-blurb">A benefit for your customer or employee! The Harlow chocolate mint is a delicious, top-of-the-line product and the perfect quick, refreshing treat.</p>
  <div class="machine-stand-photo photo" role="img" aria-label="Mint patty vending machine on a black floor stand"></div>

  <ul class="features">
    <li class="feature">
      <span class="feature__icon"><svg width="20" height="20" viewBox="0 0 22 22"><path d="M4 11l5 5 9-10" fill="none" stroke="#22a07c" stroke-width="2.5" stroke-linecap="round"/></svg></span>
      <div><p class="feature__title">FREE Placement!</p><p class="feature__text">No charge to the business owner, ever!</p></div>
    </li>
    <li class="feature">
      <span class="feature__icon"><svg width="20" height="20" viewBox="0 0 22 22"><path d="M11 2l2.7 5.6 6.1.8-4.4 4.3 1 6.1L11 16l-5.4 2.8 1-6.1L2.2 8.4l6.1-.8Z" fill="#22a07c"/></svg></span>
      <div><p class="feature__title">Sharp-looking.</p><p class="feature__text">Classy machines that take up little space. It can be placed on a stand or the counter-top. You decide!</p></div>
    </li>
    <li class="feature">
      <span class="feature__icon"><svg width="20" height="20" viewBox="0 0 22 22"><rect x="5" y="3" width="12" height="16" rx="1.5" fill="none" stroke="#22a07c" stroke-width="2"/><path d="M8 8h6M8 11h6M8 14h4" stroke="#22a07c" stroke-width="1.6"/></svg></span>
      <div><p class="feature__title">No contract.</p><p class="feature__text">Unless preferred, in which case, we have one ready to go.</p></div>
    </li>
    <li class="feature">
      <span class="feature__icon"><svg width="20" height="20" viewBox="0 0 22 22"><path d="M5 5l12 12M17 5L5 17" stroke="#22a07c" stroke-width="2.5" stroke-linecap="round"/></svg></span>
      <div><p class="feature__title">Maintenance on us!</p><p class="feature__text">Yes, we actually service our machines on a regular basis. Machines will be stocked, cleaned and are of high-quality, so no breakdowns!</p></div>
    </li>
    <li class="feature">
      <span class="feature__icon"><svg width="20" height="20" viewBox="0 0 22 22"><path d="M11 2l7 3v5c0 5-3 8-7 10-4-2-7-5-7-10V5Z" fill="none" stroke="#22a07c" stroke-width="2"/></svg></span>
      <div><p class="feature__title">No worries.</p><p class="feature__text">Zero liability for the business owner, our machines are insured.</p></div>
    </li>
  </ul>

  <div class="support-badge">
    <svg width="150" height="150" viewBox="0 0 150 150" aria-hidden="true">
      <polygon fill="#f6c518" points="150,75 136.8,91.6 140,112.5 120.3,120.3 112.5,140 91.6,136.8 75,150 58.4,136.8 37.5,140 29.7,120.3 10,112.5 13.2,91.6 0,75 13.2,58.4 10,37.5 29.7,29.7 37.5,10 58.4,13.2 75,0 91.6,13.2 112.5,10 120.3,29.7 140,37.5 136.8,58.4"/>
    </svg>
    <div class="support-badge__text">
      <p class="support-badge__head">YOUR SUPPORT HELPS VETERANS!</p>
      <p class="support-badge__note">A donation is placed directly from the Machine in your Store! Every month.</p>
    </div>
  </div>

  <div class="contact">
    <p class="contact__names">Grant and Lisa Hollis<br>Founders</p>
    <p class="contact__line">Grant: 555-014-2281 | Lisa: 555-014-7736</p>
    <p class="contact__line">Email: HollisQMT@example.com</p>
  </div>
</section>

<section class="flyer flyer--back">
  <svg class="flyer__shapes" viewBox="0 0 540 810" aria-hidden="true">
    <defs>
      <linearGradient id="headBack" x1="0" y1="0" x2="1" y2="1">
        <stop offset="0" stop-color="#2aa884"/><stop offset="1" stop-color="#137d5e"/>
      </linearGradient>
    </defs>
    <path d="M0 0H540V170C400 215 220 240 0 262Z" fill="url(#headBack)"/>
    <path d="M0 262C220 240 400 215 540 170V265C400 320 220 360 0 385Z" fill="#7fcfb0"/>
    <path d="M0 385C220 360 400 320 540 265V282C400 338 220 374 0 398Z" fill="#e4f4ee"/>
    <path d="M0 712C180 695 380 700 540 725V810H0Z" fill="#7fcfb0"/>
    <path d="M0 722C180 705 380 712 540 740V810H0Z" fill="url(#headBack)"/>
  </svg>

  <div class="brand-mark">QMT</div>
  <h2 class="back-title"><span class="back-title__small">Quill Mint</span><span class="back-title__big">Trading</span></h2>
  <p class="back-intro">Work with a local, family-owned business. If there are needs or concerns, you will speak with us!</p>

  <div class="veterans">
    <p class="veterans__head">
      <svg width="32" height="28" viewBox="0 0 32 28" aria-hidden="true"><path d="M16 26C6 19 2 14 2 8.5 2 4.9 4.9 2 8.5 2c3 0 5.2 1.7 7.5 4.5C18.3 3.7 20.5 2 23.5 2 27.1 2 30 4.9 30 8.5 30 14 26 19 16 26Z" fill="#fff"/></svg>
      <span>We happily<br>support veterans</span>
    </p>
    <p class="veterans__text">and a donation will be placed on your behalf every month a mint machine is located in your business!</p>
  </div>

  <div class="machine-photo photo" role="img" aria-label="Countertop mint patty vending machine with red base"></div>

  <div class="bonus">
    <h3 class="bonus__heading">And Get Paid?<br>Yes, Qualify for a Bonus!</h3>
    <p class="bonus__lead">Drawings for cash and prizes!</p>
    <p class="bonus__text">If your location sells specific product goals each month, the business is entered into our half-yearly drawing. Each month a location qualifies adds an additional entry!</p>
  </div>

  <p class="service-note">We find our mint patties sell best in most locations but we are a full-service vending operation with the ability to place other types of machines on request. Have questions? Have further needs? Let us know and we'll be happy to assist with any additional vending items.</p>

  <div class="chocs-photo" role="img" aria-label="Stack of chocolate mint patties"></div>

  <div class="contact">
    <p class="contact__names">Grant and Lisa Hollis<br>Founders</p>
    <p class="contact__line">Grant: 555-014-2281 | Lisa: 555-014-7736</p>
    <p class="contact__line">Email: HollisQMT@example.com</p>
  </div>
</section>

</body>
</html>
```